Design my dad a new business card because his current one sucks!

I need a business card designed for my fathers home maintenance business. His customers are individuals (single moms, old people etc.) as well as the occasional business. As such it needs to be accessible to both target audiences.

The front of the card should be dark grey on yellow with the logo and contain the following information:
- Warren Dobrinski
- 0487 362 914
- info@harbourlinehandyworks.com.au
- 0487 362 914

- ABN: 87 214 630 592
- 'Fully Insured'

The reverse should be yellow on dark grey and will have the web address:
- harbourlinehandyworks.com.au

And a few key services he offers:
GENERAL REPAIRS
PAINTING/TILING/
PAVING &CONCRETING
PRESSURE WASHING
ON-SITE WELDING
DECKING ADDITIONS & REPAIRS
FENCING
FULL BOND CLEANING

This will be first time the logo has been printed so you will need to come up with the best CMYK approximation of the RGB colours to make sure it is a close as possible.

```html
<!DOCTYPE html>
<html lang="en">
<head>
<meta charset="utf-8">
<title>Harbourline Handyworks – Business Card</title>
<link rel="stylesheet" href="https://fonts.googleapis.com/css2?family=Alegreya+Sans:wght@700&family=Michroma&display=swap">
<style>
  :root {
    --page: #ffffff;
    --card-yellow: #f7e600;
    --ink-grey: #545454;
    --ink-dark: #4a4a4a;
  }
  * { margin: 0; padding: 0; box-sizing: border-box; }
  html, body { width: 1200px; height: 900px; overflow: hidden; background: var(--page); }
  .canvas { position: relative; width: 1200px; height: 900px; background: var(--page); }
  .card-front {
    position: absolute; left: 0; top: 133px; width: 1200px; height: 667px;
    background: var(--card-yellow); overflow: hidden;
    font-family: "Alegreya Sans", "Segoe UI", sans-serif; font-weight: 700; color: var(--ink-grey);
  }
  .brand-name {
    position: absolute; left: 0; width: 100%; top: 150px;
    text-align: center; font-size: 66px; line-height: 1; color: var(--ink-dark);
  }
  .owner-name {
    position: absolute; left: 288px; top: 392px;
    font-family: "Michroma", "Verdana", sans-serif; font-weight: 400;
    font-size: 44px; line-height: 1; letter-spacing: 1px; color: var(--ink-grey);
  }
  .divider { position: absolute; left: 0; top: 0; width: 1200px; height: 667px; }
  .contact { position: absolute; display: flex; align-items: center; font-size: 34px; line-height: 1; }
  .contact svg { flex: none; }
  .contact-phone { left: 34px; top: 492px; }
  .contact-phone svg { margin-right: 26px; }
  .contact-email { left: 40px; top: 578px; font-size: 32px; }
  .contact-email svg { margin-right: 30px; }
  .business-details {
    position: absolute; left: 878px; top: 538px; font-size: 29px; line-height: 46px;
  }
</style>
</head>
<body>
<div class="canvas">
  <section class="card-front">
    <h1 class="brand-name">Harbourline Handyworks</h1>

    <svg class="divider" viewBox="0 0 1200 667" aria-hidden="true">
      <rect x="60" y="453" width="1045" height="9" fill="var(--ink-grey)"/>
      <polygon points="1098,457 1200,367 1200,549" fill="var(--ink-grey)"/>
    </svg>

    <p class="owner-name">Warren Dobrinski</p>

    <p class="contact contact-phone">
      <svg width="58" height="48" viewBox="0 0 58 48" aria-hidden="true">
        <path d="M4 14 C4 2 54 2 54 14 L54 18 L42 18 L42 12 L16 12 L16 18 L4 18 Z" fill="var(--ink-grey)"/>
        <path d="M16 16 L42 16 L52 44 L6 44 Z" fill="var(--ink-grey)"/>
        <g fill="var(--card-yellow)">
          <rect x="23" y="24" width="3" height="3"/><rect x="28" y="24" width="3" height="3"/><rect x="33" y="24" width="3" height="3"/>
          <rect x="23" y="29" width="3" height="3"/><rect x="28" y="29" width="3" height="3"/><rect x="33" y="29" width="3" height="3"/>
          <rect x="23" y="34" width="3" height="3"/><rect x="28" y="34" width="3" height="3"/><rect x="33" y="34" width="3" height="3"/>
        </g>
      </svg>
      0487 362 914
    </p>

    <p class="contact contact-email">
      <svg width="48" height="36" viewBox="0 0 48 36" aria-hidden="true">
        <rect x="1.5" y="1.5" width="45" height="33" fill="none" stroke="var(--ink-grey)" stroke-width="3"/>
        <polyline points="2,3 24,21 46,3" fill="none" stroke="var(--ink-grey)" stroke-width="3"/>
        <line x1="2" y1="34" x2="18" y2="17" stroke="var(--ink-grey)" stroke-width="3"/>
        <line x1="46" y1="34" x2="30" y2="17" stroke="var(--ink-grey)" stroke-width="3"/>
      </svg>
      info@harbourlinehandyworks.com.au
    </p>

    <div class="business-details">
      <p class="abn">ABN: 87 214 630 592</p>
      <p class="insurance">‘Fully Insured’</p>
    </div>
  </section>
</div>
</body>
</html>
```